Vision Board Class Design needed

Hello, I need a business card design for a new Company based in Mount Waverley, Victoria, Australia. The Company provides a training Class with approx. 5 guests. They learn how to choose and create positive things in their life. It is based on the principal of the Law of Attraction. Each guest receives a large coloured cardboard and magazines, affirmations to choose ideas to help create their new exciting life - all pasted onto a "Vision Board" which will be seen by them every day and help to clarify the vision and attract abundance, happiness & positivity into their lives. I would like to see designs with bright, happy colours - perhaps rainbows - anything that represents a new life and appears refreshing.
Many thanks.

Industry/Entity Type

Training

Contact Information for Business Card

Bright Horizon
Delia
Mobile 0473 206-558

Logo Text

Bright Horizon

Logo styles of interest
Abstract Logo
Requirements
Must have
• Happy, Bright colours!

```html
<!DOCTYPE html>
<html lang="en">
<head>
<meta charset="utf-8">
<title>Bright Horizon – Business Card</title>
<link rel="stylesheet" href="https://fonts.googleapis.com/css2?family=Play&family=Questrial&display=swap">
<style>
  :root {
    --backdrop: #e4e4e2;
    --card: #ffffff;
    --orange: #f9a229;
    --orange-light: #fdc776;
    --ink: #1b1b1b;
    --ink-soft: #3a3a3a;
  }
  * { box-sizing: border-box; margin: 0; padding: 0; }
  html, body {
    width: 1200px; height: 900px; overflow: hidden;
    background: var(--backdrop);
  }
  .canvas { position: relative; width: 1200px; height: 900px; }

  .card {
    position: absolute;
    width: 700px; height: 400px;
    background: var(--card);
    overflow: hidden;
    box-shadow: 0 6px 18px rgba(0,0,0,0.12);
  }
  .card--front { left: 450px; top: 50px; }
  .card--back  { left: 50px;  top: 470px; }

  .card__band { position: absolute; inset: 0; width: 100%; height: 100%; }
  .band-light { fill: var(--orange-light); }
  .band-main  { fill: var(--orange); }

  .brand-dot {
    position: absolute;
    border-radius: 50%;
    background: var(--orange);
  }
  .brand-name {
    position: absolute;
    font-family: "Play", sans-serif;
    font-weight: 400;
    color: var(--ink);
    white-space: nowrap;
    transform: translateX(-50%);
  }

  .card--front .brand-dot { width: 110px; height: 110px; left: 345px; top: 45px; }
  .card--front .brand-name { left: 390px; top: 170px; font-size: 48px; letter-spacing: 2px; }

  .card--back .brand-dot { width: 150px; height: 150px; left: 455px; top: 70px; }
  .card--back .brand-name { left: 530px; top: 250px; font-size: 26px; letter-spacing: 1px; }

  .holder { position: absolute; left: 45px; top: 40px; font-family: "Questrial", sans-serif; }
  .holder__name { font-size: 40px; color: var(--ink); line-height: 1; }
  .holder__role { font-size: 15px; color: var(--ink-soft); margin-top: 4px; }

  .contact-list {
    position: absolute; left: 45px; top: 160px;
    list-style: none;
    font-family: "Questrial", sans-serif;
    font-size: 22px; color: var(--ink);
  }
  .contact-list li { display: flex; align-items: center; gap: 14px; height: 44px; }
  .contact-icon { width: 28px; height: 28px; flex: none; }
  .icon-stroke { fill: none; stroke: var(--orange); stroke-width: 2; }
  .icon-fill { fill: var(--orange); }
</style>
</head>
<body>
<main class="canvas">

  <section class="card card--front" aria-label="Card front">
    <svg class="card__band" viewBox="0 0 700 400" preserveAspectRatio="none" aria-hidden="true">
      <path class="band-light" d="M0,300 Q350,350 700,255 L700,400 L0,400 Z"/>
      <path class="band-main" d="M0,315 Q350,370 700,275 L700,400 L0,400 Z"/>
    </svg>
    <span class="brand-dot" aria-hidden="true"></span>
    <span class="brand-name">Bright Horizon</span>
  </section>

  <section class="card card--back" aria-label="Card back">
    <svg class="card__band" viewBox="0 0 700 400" preserveAspectRatio="none" aria-hidden="true">
      <path class="band-light" d="M0,318 Q350,368 700,290 L700,400 L0,400 Z"/>
      <path class="band-main" d="M0,333 Q350,388 700,308 L700,400 L0,400 Z"/>
    </svg>

    <div class="holder">
      <p class="holder__name">Delia</p>
      <p class="holder__role">manager</p>
    </div>

    <ul class="contact-list">
      <li>
        <svg class="contact-icon" viewBox="0 0 28 28" aria-hidden="true">
          <circle class="icon-stroke" cx="14" cy="14" r="12"/>
          <path class="icon-fill" d="M10 8.5c.6-.6 1.4-.5 1.8.1l1.2 1.8c.3.5.2 1.1-.2 1.5l-.8.7c.6 1.4 1.6 2.5 3 3.2l.7-.8c.4-.4 1-.5 1.5-.2l1.8 1.1c.6.4.7 1.2.2 1.8l-.9.9c-.8.8-2.1 1-3.1.4-2.8-1.5-4.9-3.7-6.3-6.5-.5-1-.3-2.2.5-3z"/>
        </svg>
        <span>0473 206-558</span>
      </li>
      <li>
        <svg class="contact-icon" viewBox="0 0 28 28" aria-hidden="true">
          <circle class="icon-stroke" cx="14" cy="14" r="12"/>
          <rect class="icon-stroke" x="7.5" y="9.5" width="13" height="9" stroke-width="1.6"/>
          <path class="icon-stroke" d="M7.5 9.5 L14 15 L20.5 9.5" stroke-width="1.6"/>
        </svg>
        <span>delia@brighthorizon.com</span>
      </li>
      <li>
        <svg class="contact-icon" viewBox="0 0 28 28" aria-hidden="true">
          <path class="icon-fill" d="M14 2a8 8 0 0 0-8 8c0 6 8 16 8 16s8-10 8-16a8 8 0 0 0-8-8zm0 11a3 3 0 1 1 0-6 3 3 0 0 1 0 6z"/>
        </svg>
        <span>street 58 building no 14</span>
      </li>
    </ul>

    <span class="brand-dot" aria-hidden="true"></span>
    <span class="brand-name">Bright Horizon</span>
  </section>

</main>
</body>
</html>
```